Trade Show Banner "Brindlequay"

1.7' x 3' vertical banner to complement trade show booth panels (3-panel tabletop booth attached). The word file (attached) is for text and not meant to imply design. We manage homeowner and condo associations that are run by volunteer boards of directors who already have full-time jobs or who may have no training in how to run an organization. It can be highly stressful and not very rewarding. We want this poster/banner to convey that feeling of stress along with a hope for relief and relaxation. Our logo is attached. The full logo is the top one in the file. You may also want to use the triangle (attached) in addition to or instead of the logo. Our corporate fonts are attached. Please let me know if you need additional information or if you feel like there is too much copy or any other thoughts or comments you have.

Target Market(s)

Volunteer boards of directors for homeowner and condo associations--all ages, genders, races, occupations.

Industry/Entity Type

Property Management

Other font styles liked:
• "Copper Lantern" is part of a trademark and should be in Mistral with the green from our logo

Requirements
Must have
• Simple, easy to read, don't clash with booth design
Nice to have
• convey the tension of stress contrasted with the feeling of relaxation and relief.

```html
<!DOCTYPE html>
<html lang="en">
<head>
<meta charset="utf-8">
<title>The Art of Brindlequay for Board Members</title>
<link rel="stylesheet" href="https://fonts.googleapis.com/css2?family=Lobster&family=Dancing+Script:wght@600&family=Andika:wght@400;700&family=Mukta:wght@500;600&display=swap">
<style>
  :root {
    --backdrop: #414042;
    --paper: #ffffff;
    --navy: #26235e;
    --green: #1f6e35;
    --maroon: #7a1421;
    --ink: #3a3a3a;
    --band: #ececec;
    --sky-top: #b9c3cf;
    --sky-mid: #e3e7ec;
  }
  * { box-sizing: border-box; margin: 0; padding: 0; }
  html, body { width: 960px; height: 1200px; overflow: hidden; }
  body { background: var(--backdrop); position: relative; font-family: "Andika", sans-serif; }

  .banner {
    position: absolute; left: 197px; top: 78px;
    width: 592px; height: 1045px;
    background: var(--paper); overflow: hidden;
  }

  .hero {
    position: absolute; left: 0; top: 0; width: 100%; height: 276px;
    background:
      linear-gradient(to bottom, rgba(255,255,255,0) 55%, #fff 100%),
      linear-gradient(to bottom, var(--sky-top) 0%, var(--sky-mid) 45%, #cfd9e0 58%, #eef0f1 72%, #fff 100%);
  }
  .hero-photo {
    position: absolute; right: 20px; top: 100px; width: 170px; height: 150px;
    background: radial-gradient(ellipse at 50% 50%, rgba(150,140,135,.35), rgba(255,255,255,0) 70%);
  }
  .title-lead, .title-tail {
    position: absolute; left: 27px; color: var(--navy);
    font-family: "Mukta", sans-serif; font-weight: 600; line-height: 1;
  }
  .title-lead { top: 76px; font-size: 36px; }
  .title-tail { top: 198px; font-size: 32px; }
  .title-main {
    position: absolute; left: 24px; top: 108px;
    font-family: "Lobster", cursive; font-size: 68px; line-height: 1;
    color: var(--green);
    text-shadow: 0 0 2px #fff, 2px 2px 0 #fff, -2px -2px 0 #fff, 2px -2px 0 #fff, -2px 2px 0 #fff, 3px 4px 4px rgba(0,0,0,.35);
  }

  .pair {
    position: absolute; left: 0; width: 100%;
    background: linear-gradient(to right, var(--band) 0%, #f4f4f4 60%, #fff 100%);
    padding: 18px 33px 0;
  }
  .stress {
    font-family: "Mukta", sans-serif; font-weight: 600; font-size: 18.5px;
    color: var(--maroon); line-height: 1.2;
  }
  .relief {
    margin-top: 14px; font-size: 20px; line-height: 29px; color: var(--ink);
  }
  .relax-word { font-family: "Lobster", cursive; color: var(--green); font-size: 23px; }
  .trademark { font-family: "Dancing Script", cursive; color: var(--green); font-size: 19px; }

  .p1 { top: 276px; height: 99px; }
  .p2 { top: 380px; height: 98px; }
  .p3 { top: 482px; height: 98px; }
  .p4 { top: 584px; height: 134px; }
  .p5 { top: 722px; height: 182px; }

  .cta {
    position: absolute; left: 33px; top: 935px;
    font-family: "Mukta", sans-serif; font-weight: 600; font-size: 26px; line-height: 35px;
    color: var(--navy);
  }
  .cta .relax-word { font-size: 28px; }

  .brand {
    position: absolute; right: 28px; top: 960px;
    display: flex; align-items: center; gap: 8px;
    font-family: "Mukta", sans-serif; font-weight: 500; font-size: 13.5px;
    color: var(--navy); letter-spacing: .3px;
  }
  .brand-mark { width: 12px; height: 12px; background: var(--maroon); }
</style>
</head>
<body>
  <main class="banner">
    <div class="hero">
      <div class="hero-photo" role="img" aria-label="Photo of a businessman relaxing in a beach chair by the sea"></div>
    </div>
    <h1>
      <span class="title-lead">The Art of</span>
      <span class="title-main">Brindlequay</span>
      <span class="title-tail">for Board Members</span>
    </h1>

    <section class="pair p1">
      <p class="stress">Stress: THE BOARD HAS TOO MUCH WORK TO DO</p>
      <p class="relief"><span class="relax-word">Relax…</span>and let us do the work.</p>
    </section>
    <section class="pair p2">
      <p class="stress">Stress: YOUR COMMUNITY HAS “ISSUES”.</p>
      <p class="relief"><span class="relax-word">Relax…</span>and let us give you a <span class="trademark">Copper Lantern.</span></p>
    </section>
    <section class="pair p3">
      <p class="stress">Stress: YOUR MEMBERS CANNOT PAY ONLINE.</p>
      <p class="relief"><span class="relax-word">Relax…</span>we’ll give your members multiple ways to pay.</p>
    </section>
    <section class="pair p4">
      <p class="stress">Stress: COMMUNICATION IS POOR OR INCONSISTENT.</p>
      <p class="relief"><span class="relax-word">Relax…</span>we’ll keep you informed with a robust online portal, chock full of information.</p>
    </section>
    <section class="pair p5">
      <p class="stress">Stress: YOUR DELINQUENCIES ARE HIGH.</p>
      <p class="relief"><span class="relax-word">Relax…</span>as a licensed collection agency, we have developed an effective collections program that works in tandem with your collections attorney. Plus, we can report to the credit bureau!</p>
    </section>

    <p class="cta">COME IN TO TALK AND<br>START <span class="relax-word">Relaxing</span> TODAY!</p>

    <div class="brand">
      <span class="brand-mark"></span>
      <span>TESSMERE MANAGEMENT, INC.</span>
    </div>
  </main>
</body>
</html>
```